Add words, element to an already make product design

Hi guys,
I m already have the design (attached) which is a wet tissue product. The front main side (about 14cm x 7 cm) is the waves and the brand name Zelfo. However, in this main side, it should contain more words, which are "Khan uot" (mean wet wipe), and the words "Mat lanh" (mean cooling) and "Tinh khiet" (mean purity). "Khan uot" to indicate function of the product, while Mat lanh and Tinh khiet are just marketing term to add.
So yes, the task is quite simple, but I think the key is to choose an appropriate font, color and the location you decide where it should be. You can add any element you want, as long as it look good overall, and those words above, are required to have. More in the attached are few rival from our market, as some example.
Thank you, and wait your idea.

Hi guys, Just to tell you that the main front design will not change. So the waves and the brand name still keep the same. Just adding more words or elements to it. Thank you guys.

```html
<!DOCTYPE html>
<html lang="vi">
<head>
<meta charset="utf-8">
<title>Zelfo – Khăn ướt – dieline</title>
<link rel="stylesheet" href="https://fonts.googleapis.com/css2?family=Nunito:wght@600;800;900&family=Arimo:wght@400;700&display=swap">
<style>
  :root{
    --paper:#ffffff;
    --ink:#111111;
    --guide:#555555;
    --brand:#1b8fcf;
    --sea-light:#cfe7f5;
    --sea-mid:#4aa9dc;
    --sea-deep:#1670b8;
    --tag-light:#9fc9e6;
    --tag-deep:#5c9fd1;
    --back-ink:#2b6fae;
  }
  html,body{margin:0;padding:0;width:1200px;height:1200px;overflow:hidden;background:var(--paper);}
  .sheet{position:relative;width:1200px;height:1200px;font-family:"Nunito",sans-serif;}
  .guides{position:absolute;inset:0;}
  .dim{font-family:"Arimo",sans-serif;fill:var(--ink);}
  .artwork{position:absolute;left:276px;top:264px;width:648px;height:672px;overflow:hidden;}
  .waves{position:absolute;left:0;top:0;width:648px;height:672px;}
  .claim{position:absolute;font-weight:900;font-size:26px;letter-spacing:2px;
    background:linear-gradient(90deg,var(--tag-light),var(--tag-deep));
    -webkit-background-clip:text;background-clip:text;color:transparent;white-space:nowrap;}
  .claim-purity{left:386px;top:206px;}
  .claim-cooling{left:452px;top:254px;}
  .claim-icon{position:absolute;}
  .brand-name{position:absolute;left:0;width:648px;top:290px;text-align:center;
    font-weight:900;font-size:100px;color:var(--brand);line-height:1;letter-spacing:1px;}
  .product-type{position:absolute;left:222px;top:398px;font-weight:800;font-size:30px;color:#fff;
    letter-spacing:2px;transform:rotate(-5deg);white-space:nowrap;}
  .back-note{position:absolute;left:50px;top:42px;font-family:"Arimo",sans-serif;font-size:7px;
    line-height:9px;color:var(--back-ink);width:60px;}
  .usage-icons{position:absolute;left:84px;top:26px;display:grid;grid-template-columns:repeat(3,22px);gap:12px 14px;}
  .usage-icons span{width:22px;height:22px;border:1.5px solid var(--back-ink);border-radius:4px;box-sizing:border-box;}
  .usage-icon-extra{position:absolute;left:82px;top:96px;width:20px;height:20px;border:1.5px solid var(--back-ink);border-radius:4px;box-sizing:border-box;}
  .dates{position:absolute;left:206px;top:30px;font-family:"Arimo",sans-serif;font-size:8px;line-height:10px;color:var(--back-ink);}
  .quality-seal{position:absolute;left:508px;top:32px;}
  .code-box{position:absolute;left:375px;top:538px;width:183px;height:74px;background:#fff;}
  .hb-tab{position:absolute;left:216px;top:946px;width:22px;height:50px;background:var(--sea-mid);}
</style>
</head>
<body>
<div class="sheet">

  <div class="artwork">
    <svg class="waves" viewBox="0 0 648 672" role="img" aria-label="Watercolour blue ocean waves rising from light to deep blue">
      <defs>
        <linearGradient id="sea" x1="0" y1="0" x2="0" y2="1">
          <stop offset="0" stop-color="var(--sea-light)"/>
          <stop offset="0.35" stop-color="var(--sea-mid)"/>
          <stop offset="1" stop-color="var(--sea-deep)"/>
        </linearGradient>
      </defs>
      <path d="M0 300 C120 250 220 330 360 300 C470 275 560 300 648 330 L648 672 L0 672 Z" fill="url(#sea)"/>
    </svg>

    <div class="back-note">Lau tay sạch<br>Dùng một lần</div>
    <div class="usage-icons"><span></span><span></span><span></span><span></span><span></span><span></span></div>
    <div class="usage-icon-extra"></div>
    <div class="dates">NSX: 2 năm trước HSD<br>HSD: In trên bao bì</div>
    <svg class="quality-seal" width="118" height="96" viewBox="0 0 118 96">
      <path d="M4 4 H114 V66 L59 92 L4 66 Z" fill="none" stroke="var(--back-ink)" stroke-width="3"/>
    </svg>

    <div class="claim claim-purity">Tinh khiet</div>
    <svg class="claim-icon" style="left:554px;top:208px" width="16" height="24" viewBox="0 0 16 24">
      <path d="M8 1 C4 9 1 13 1 16 A7 7 0 0 0 15 16 C15 13 12 9 8 1 Z" fill="var(--tag-deep)"/>
    </svg>
    <div class="claim claim-cooling">Mat lanh</div>
    <svg class="claim-icon" style="left:584px;top:258px" width="24" height="24" viewBox="0 0 24 24" stroke="var(--tag-deep)" stroke-width="2" stroke-linecap="round">
      <line x1="12" y1="2" x2="12" y2="22"/><line x1="3.3" y1="7" x2="20.7" y2="17"/><line x1="3.3" y1="17" x2="20.7" y2="7"/>
    </svg>

    <div class="brand-name">Zelfo</div>
    <div class="product-type">Khăn ướt</div>

    <div class="code-box"></div>
  </div>

  <div class="hb-tab"></div>

  <svg class="guides" width="1200" height="1200" viewBox="0 0 1200 1200">
    <g stroke="var(--guide)" stroke-width="1.5" stroke-dasharray="9 6" fill="none">
      <line x1="216" y1="185" x2="216" y2="1000"/>
      <line x1="276" y1="185" x2="276" y2="1000"/>
      <line x1="924" y1="185" x2="924" y2="1000"/>
      <line x1="984" y1="185" x2="984" y2="1000"/>
      <line x1="216" y1="204" x2="1000" y2="204"/>
      <line x1="216" y1="264" x2="1000" y2="264"/>
      <line x1="216" y1="432" x2="1000" y2="432"/>
      <line x1="216" y1="768" x2="1000" y2="768"/>
      <line x1="216" y1="936" x2="1000" y2="936"/>
      <line x1="216" y1="996" x2="1000" y2="996"/>
    </g>
    <g class="dim" font-size="22" text-anchor="middle">
      <text x="246" y="180">12.5</text>
      <text x="600" y="180" font-size="28">135</text>
      <text x="954" y="180">12.5</text>
      <text x="600" y="1050" font-size="28">160 mm</text>
      <text transform="translate(190 600) rotate(-90)" font-size="26">165mm</text>
      <text transform="translate(1012 234) rotate(90)" font-size="18">12.5</text>
      <text transform="translate(1012 348) rotate(90)" font-size="18">35</text>
      <text transform="translate(1012 600) rotate(90)" font-size="18">70</text>
      <text transform="translate(1012 852) rotate(90)" font-size="18">35</text>
      <text transform="translate(1012 966) rotate(90)" font-size="18">12.5</text>
    </g>
  </svg>

</div>
</body>
</html>
```